Online Tech Store Needs New Banner Ads

We need two new banner ads (two designs in two sizes). HTML5. Simple no-fuss design. Clean, professional.

We are QuillTag (quilltagstore.net), an online retailer of NFC tags and products. We run the ads through industry specific websites. We need a leaderboard and 300x250.

First ad should be a promo of our 'NFC Starter Packs / Order online now'. Graphics have been uploaded. Second, should be 'Large range of NFC tags in stock / fast delivery / order online now'.

We have uploaded a couple of generic photos for ideas. However, any image from our website can be used and we can supply high-res if required.

Target Market(s)

General. But general tech.

Industry/Entity Type

Information Technology

Font styles to use
Sans Serif

Requirements
Must have
• Clear, clean, professional design. Follow our corporate logo colours.
• Include our company logo and the NFC logo 'N)) NFC' graphic (uploaded). Company logo must be in colour. 'N))' logo can be any colour/grey/black and can also have transparency. Would suggest that 'N))' is small.
• Include call to action (buy online now) but nothing too big / cheap looking.
• Only two sizes required at the moment - Leaderboard and 300x250.
Should not have
• Anything that looks messy !

```html
<!DOCTYPE html>
<html lang="en">
<head>
<meta charset="utf-8">
<title>QuillTag – Large range of NFC tags in stock</title>
<link rel="stylesheet" href="https://fonts.googleapis.com/css2?family=PT+Sans+Narrow:wght@700&family=Patrick+Hand&display=swap">
<style>
  :root {
    --brand-green: #86982a;
    --ink: #1c1c1c;
    --mark-grey: #8a8a8a;
    --tag-dark: #6e6f71;
    --tag-light: #c9cacc;
    --paper: #ffffff;
  }
  * { margin: 0; padding: 0; box-sizing: border-box; }
  html, body {
    width: 1200px;
    height: 276px;
    overflow: hidden;
    background: var(--paper);
  }
  .leaderboard {
    position: relative;
    width: 1200px;
    height: 276px;
    background: var(--paper);
    overflow: hidden;
  }
  .headline {
    position: absolute;
    left: 32px;
    top: 24px;
    font-family: "PT Sans Narrow", "Arial Narrow", sans-serif;
    font-weight: 700;
    font-size: 49px;
    line-height: 1;
    color: var(--brand-green);
    white-space: nowrap;
  }
  .tagline {
    position: absolute;
    left: 32px;
    top: 90px;
    font-family: "Patrick Hand", "Comic Sans MS", cursive;
    font-size: 46px;
    line-height: 1;
    color: var(--ink);
    white-space: nowrap;
  }
  .cta {
    position: absolute;
    left: 32px;
    top: 178px;
    width: 294px;
    height: 62px;
    border: 3px solid var(--brand-green);
    padding: 4px;
    text-decoration: none;
  }
  .cta-inner {
    display: flex;
    align-items: center;
    justify-content: center;
    width: 100%;
    height: 100%;
    border: 1.5px solid var(--brand-green);
    font-family: "PT Sans Narrow", "Arial Narrow", sans-serif;
    font-weight: 700;
    font-size: 30px;
    color: var(--brand-green);
    white-space: nowrap;
  }
  .product-visual {
    position: absolute;
    left: 690px;
    top: 8px;
    width: 150px;
    height: 250px;
    border-radius: 75px 75px 75px 75px / 80px 80px 75px 75px;
    background: linear-gradient(180deg, var(--tag-light) 0%, #a4a5a7 45%, var(--tag-dark) 100%);
  }
  .standard-mark {
    position: absolute;
    left: 1048px;
    top: 104px;
    display: flex;
    align-items: center;
    gap: 8px;
    font-family: "PT Sans Narrow", "Arial Narrow", sans-serif;
    font-weight: 700;
    font-size: 28px;
    line-height: 1;
    color: var(--mark-grey);
    white-space: nowrap;
  }
  .standard-mark .dot {
    width: 12px;
    height: 12px;
    border-radius: 50%;
    background: var(--mark-grey);
  }
  .brand {
    position: absolute;
    left: 944px;
    top: 200px;
    display: flex;
    align-items: center;
    gap: 12px;
    font-family: "PT Sans Narrow", "Arial Narrow", sans-serif;
    font-weight: 700;
    font-size: 46px;
    line-height: 1;
    color: var(--brand-green);
    white-space: nowrap;
  }
  .brand .square {
    width: 16px;
    height: 16px;
    background: var(--brand-green);
  }
</style>
</head>
<body>
  <main class="leaderboard">
    <h1 class="headline">Large range of NFC tags in stock</h1>
    <p class="tagline">fast delivery</p>
    <a class="cta" href="https://quilltagstore.net">
      <span class="cta-inner">Order Online Now</span>
    </a>

    <div class="product-visual" role="img" aria-label="Photo of a round grey NFC key-fob tag hanging from a black cord loop"></div>

    <div class="standard-mark">
      <span class="dot"></span>
      <span>Tagvell</span>
    </div>

    <div class="brand">
      <span class="square"></span>
      <span>QuillTag</span>
    </div>
  </main>
</body>
</html>
```